Desing for real estate offers- Package system

The word should be graphically clear and understandable. There are 3 packages that the customer can buy: the basic package is red, the medicinal package is green and the carefree package is blue. See the Word document in the appendix. End file should be a Word, as we need to chance the text. It should also match the website as well as the business card.
https://brelvona.domistra.ch/
Colors:
Green 1: R: 187, G: 214, B: 49
Green 2: R: 119, G: 187, W: 66

Target Market(s)

Real estate company

Font styles to use
Serif
Sans Serif

```html
<!DOCTYPE html>
<html lang="de">
<head>
<meta charset="utf-8">
<title>Brelvona – Individuelle Vermarktungspakete</title>
<link href="https://fonts.googleapis.com/css2?family=Arimo:wght@400;500&family=Roboto+Condensed:wght@400;500&display=swap" rel="stylesheet">
<style>
  :root{
    --green-1:#bbd631;
    --green-2:#77bb42;
    --green-table:#7ac143;
    --orange:#fbb040;
    --teal:#13a89e;
    --grey-cell:#f1f1f1;
    --grey-line:#d4d4d4;
    --text-dark:#3a3a3a;
    --page-bg:#e9e9e7;
    --white:#ffffff;
  }
  *{box-sizing:border-box;margin:0;padding:0}
  html,body{width:1200px;height:801px;overflow:hidden;background:var(--page-bg)}
  .flyer{
    position:absolute;left:324px;top:8px;width:594px;height:843px;
    transform:scale(0.93);transform-origin:0 0;
    background:var(--white);box-shadow:0 2px 10px rgba(0,0,0,.18);
    font-family:"Arimo",Arial,sans-serif;overflow:hidden;
  }
  .hero{position:absolute;left:0;top:0;width:594px;height:316px}
  .hero-photo{
    position:absolute;left:0;top:0;width:300px;height:316px;
    background:linear-gradient(180deg,#dfe1dc 0%,#b8c4ae 40%,#7fae4a 75%,#5f9a2e 100%);
  }
  .brand-band{position:absolute;left:300px;top:0;width:294px;height:85px;background:var(--white)}
  .title-panel{position:absolute;left:300px;top:85px;width:294px;height:231px;background:var(--green-2)}
  .brand-name{
    position:absolute;right:17px;top:32px;
    font-family:"Arimo",Arial,sans-serif;font-weight:500;font-size:33px;color:var(--green-2);letter-spacing:.5px;
  }
  .hero-title{
    position:absolute;right:17px;top:128px;text-align:right;color:var(--white);
    font-family:"Roboto Condensed",sans-serif;font-weight:500;font-size:25px;line-height:31px;
  }
  .hero-rule{position:absolute;right:17px;top:195px;width:116px;height:3px;background:var(--white)}
  .hero-note{
    position:absolute;right:17px;top:218px;text-align:right;color:var(--white);
    font-size:13.2px;line-height:17px;white-space:nowrap;
  }
  .packages{
    position:absolute;left:20px;top:332px;width:558px;
    display:grid;grid-template-columns:227px 111px 110px 110px;
    font-family:"Roboto Condensed",sans-serif;box-shadow:0 2px 4px rgba(0,0,0,.12);
  }
  .packages > div{display:flex;align-items:center}
  .task{background:var(--grey-cell);border-bottom:1px solid var(--grey-line);padding:0 12px;font-size:8.6px;line-height:9.5px;color:var(--text-dark);height:16.7px}
  .task.double{height:25px}
  .head{height:50px;justify-content:center;text-align:center;color:var(--white);font-size:8.6px;line-height:10px}
  .head.task{justify-content:flex-start;color:var(--green-2);font-size:11px;height:50px}
  .basis{background:var(--orange)}
  .medium{background:var(--teal)}
  .sorglos{background:var(--green-table)}
  .tick{justify-content:center;color:var(--white);font-size:12px;border-bottom:1px solid rgba(255,255,255,.35)}
  .head.sorglos{font-size:7.2px;line-height:8.4px;padding:0 3px}
  .footer{
    position:absolute;left:0;top:798px;width:594px;height:45px;background:var(--green-2);
    display:flex;align-items:center;justify-content:space-between;padding:0 22px;
    color:var(--white);font-size:14px;letter-spacing:.3px;
  }
  .contact{display:flex;align-items:center;gap:6px}
  .contact svg{width:13px;height:13px}
</style>
</head>
<body>
<article class="flyer">
  <header class="hero">
    <div class="hero-photo" role="img" aria-label="Foto eines hellen, modern eingerichteten Wohnzimmers mit grünem Sofa und Pouf"></div>
    <div class="brand-band"></div>
    <div class="title-panel"></div>
    <div class="brand-name">Brelvona</div>
    <h1 class="hero-title">INDIVIDUELLE<br>VERMARKTUNGSPAKETE</h1>
    <div class="hero-rule"></div>
    <p class="hero-note">Unterlagen müssen gestellt werden, ansonsten<br>werden Sie 1:1 verrechnet: GB-Auszug,GVZ,<br>Nebenkostenabrechnung, STWEG-Protokolle<br>der letzten 3 Jahren, …</p>
  </header>

  <section class="packages">
    <div class="task head">VERKAUFSABLAUF:</div>
    <div class="head basis">Basis-Paket<br>8'500.- CHF exkl. MWST</div>
    <div class="head medium">Medium-Paket<br>10'900 CHF exkl. MWST</div>
    <div class="head sorglos">Sorglos: 2% vom<br>Verkaufspreis inkl. MWST<br>(von Grundstückgewinnsteuer<br>abziehbar)</div>

    <div class="task">Begehung Verkaufsobjekt</div><div class="tick basis">✓</div><div class="tick medium">✓</div><div class="tick sorglos">✓</div>
    <div class="task">Hedonische Schätzung intern &amp; Bank</div><div class="tick basis">✓</div><div class="tick medium">✓</div><div class="tick sorglos">✓</div>
    <div class="task">Marketing &amp; Vertriebskonzept</div><div class="tick basis">✓</div><div class="tick medium">✓</div><div class="tick sorglos">✓</div>
    <div class="task double">Unterlagen einfordern- STWEG Protokolle,<br>GB Auszug u.s.w wenn nötig</div><div class="tick basis">✓</div><div class="tick medium">✓</div><div class="tick sorglos">✓</div>
    <div class="task">Fotografieren &amp; Ausmessen der Immobilie</div><div class="tick basis">✓</div><div class="tick medium">✓</div><div class="tick sorglos">✓</div>
    <div class="task">Grundriss zeichnen</div><div class="tick basis">✓</div><div class="tick medium">✓</div><div class="tick sorglos">✓</div>
    <div class="task">Dokumentation erstellen</div><div class="tick basis">✓</div><div class="tick medium">✓</div><div class="tick sorglos">✓</div>
    <div class="task">Unsere Interessenten anschreiben</div><div class="tick basis"></div><div class="tick medium">✓</div><div class="tick sorglos">✓</div>
    <div class="task">Immobilie Online aufbereiten &amp; Aufschalten</div><div class="tick basis">✓</div><div class="tick medium">✓</div><div class="tick sorglos">✓</div>
    <div class="task">Anfragen beantworten- telefonisch &amp; elektronisch</div><div class="tick basis"></div><div class="tick medium">✓</div><div class="tick sorglos">✓</div>
    <div class="task">Besichtigungen koordinieren</div><div class="tick basis"></div><div class="tick medium"></div><div class="tick sorglos">✓</div>
    <div class="task">Besichtigungen Durchführen</div><div class="tick basis"></div><div class="tick medium"></div><div class="tick sorglos">✓</div>
    <div class="task">Interessenten &amp; Kaufangebote prüfen</div><div class="tick basis">✓</div><div class="tick medium">✓</div><div class="tick sorglos">✓</div>
    <div class="task">Evt. Bieterverfahren modern oder altmodisch</div><div class="tick basis"></div><div class="tick medium">✓</div><div class="tick sorglos">✓</div>
    <div class="task">Käufer zusage- andere noch vertrösten</div><div class="tick basis">✓</div><div class="tick medium">✓</div><div class="tick sorglos">✓</div>
    <div class="task">Sicherheitsnachweis (SINA)- organisieren</div><div class="tick basis"></div><div class="tick medium"></div><div class="tick sorglos">✓</div>
    <div class="task">Erstellung erster Kaufvertragsentwurf</div><div class="tick basis">✓</div><div class="tick medium">✓</div><div class="tick sorglos">✓</div>
    <div class="task double">Berechnung provisorische<br>Grundstückgewinnsteuer- Steueramt</div><div class="tick basis"></div><div class="tick medium"></div><div class="tick sorglos">✓</div>
    <div class="task">Beurkundungstermin vereinbaren</div><div class="tick basis"></div><div class="tick medium"></div><div class="tick sorglos">✓</div>
    <div class="task">Begleitung aufs Notariat</div><div class="tick basis"></div><div class="tick medium">✓</div><div class="tick sorglos">✓</div>
    <div class="task">Eigentumsübertragung vereinbaren</div><div class="tick basis"></div><div class="tick medium"></div><div class="tick sorglos">✓</div>
    <div class="task double">Helfen bei der Steuererklärung für die definitive<br>Grundstückgewinnsteuer</div><div class="tick basis"></div><div class="tick medium"></div><div class="tick sorglos">✓</div>
  </section>

  <footer class="footer">
    <span class="contact"><svg viewBox="0 0 14 14" aria-hidden="true"><circle cx="7" cy="7" r="6" fill="none" stroke="#fff" stroke-width="1.4"/><rect x="4" y="5" width="6" height="4" fill="#fff"/></svg>info@brelvona.ch</span>
    <span class="contact"><svg viewBox="0 0 14 14" aria-hidden="true"><circle cx="7" cy="7" r="6" fill="none" stroke="#fff" stroke-width="1.4"/><path d="M4.5 4 L6 4 L6.5 6 L5.6 6.7 Q6.5 8.4 7.8 8.8 L8.5 8 L10 8.5 L10 10 Q6 10.5 4.5 4 Z" fill="#fff"/></svg>+41 44 000 12 34</span>
    <span class="contact"><svg viewBox="0 0 14 14" aria-hidden="true"><circle cx="7" cy="7" r="6" fill="none" stroke="#fff" stroke-width="1.4"/><ellipse cx="7" cy="7" rx="2.4" ry="6" fill="none" stroke="#fff" stroke-width="1"/><line x1="1" y1="7" x2="13" y2="7" stroke="#fff" stroke-width="1"/></svg>www.brelvona.ch</span>
  </footer>
</article>
</body>
</html>
```